Dorsey K. Wendell Business Card

We need a business card for our company Dorsey K. Wendell Heating & Plumbing to be distributed to potential customers. It should follow the color scheme of our logo and have a modern upscale and masculine look.

The logo is attached and the info below should also be included:

5187 W. Cedar Brook Rd.
Larkston, PA 17632

Russell T. Wendell
(717) 592-0817
russelltwendell@fernmail.net
dorseykwendell.net
PA #093148

Industry/Entity Type

Business

Contact Information for Business Card

5187 W. Cedar Brook Rd.
Larkston, PA 17632

Russell T. Wendell
(717) 592-0817
russelltwendell@fernmail.net
dorseykwendell.net
PA #093148

Colors

Designer to choose colors to be used in the design.

Requirements
Must have
• Information above included

```html
<!DOCTYPE html>
<html lang="en">
<head>
<meta charset="utf-8">
<title>Dorsey K. Wendell Business Card</title>
<link rel="stylesheet" href="https://fonts.googleapis.com/css2?family=Exo+2:wght@400;500;600;700&display=swap">
<style>
  :root {
    --brand-blue: #1856a6;
    --brand-green: #9cc825;
    --text-grey: #8a8a8a;
    --card-white: #ffffff;
    --canvas-bg: #e4e5e7;
  }
  * { box-sizing: border-box; margin: 0; padding: 0; }
  html, body { width: 1200px; height: 900px; overflow: hidden; }
  body {
    background: var(--canvas-bg);
    font-family: "Exo 2", sans-serif;
    position: relative;
  }
  .card {
    position: absolute;
    left: 320px;
    width: 560px;
    height: 320px;
    box-shadow: 0 6px 18px rgba(0,0,0,0.18);
  }
  /* Back of card */
  .card-back {
    top: 90px;
    background: var(--brand-blue);
    display: flex;
    align-items: center;
    justify-content: center;
  }
  .back-lockup {
    display: flex;
    align-items: center;
    gap: 14px;
  }
  .back-square {
    width: 58px;
    height: 58px;
    background: var(--card-white);
  }
  .back-words { display: flex; flex-direction: column; }
  .back-name {
    color: var(--card-white);
    font-weight: 700;
    font-size: 30px;
    letter-spacing: 2px;
    text-transform: uppercase;
    line-height: 1.1;
    padding-bottom: 6px;
    border-bottom: 1px solid var(--brand-green);
  }
  .back-trade {
    color: var(--brand-green);
    font-weight: 700;
    font-size: 13px;
    letter-spacing: 1.5px;
    text-transform: uppercase;
    text-align: right;
    padding-top: 5px;
  }
  /* Front of card */
  .card-front {
    top: 490px;
    background: var(--card-white);
  }
  .front-mark {
    position: absolute;
    left: 40px;
    top: 110px;
    display: flex;
    align-items: center;
    gap: 10px;
  }
  .front-square {
    width: 110px;
    height: 110px;
    background: var(--brand-blue);
  }
  .front-company {
    color: var(--brand-blue);
    font-weight: 700;
    font-size: 15px;
    letter-spacing: 1px;
    text-transform: uppercase;
    line-height: 1.25;
    width: 110px;
  }
  .contact {
    position: absolute;
    right: 32px;
    top: 28px;
    text-align: right;
  }
  .person-name {
    color: var(--brand-blue);
    font-weight: 600;
    font-size: 20px;
    letter-spacing: 1.5px;
    text-transform: uppercase;
  }
  .person-title {
    color: var(--brand-green);
    font-weight: 500;
    font-size: 13px;
    letter-spacing: 1.5px;
    text-transform: uppercase;
  }
  .license {
    color: var(--brand-blue);
    font-size: 13px;
    letter-spacing: 1.5px;
    margin-top: 38px;
  }
  .address {
    color: var(--text-grey);
    font-size: 15px;
    font-style: normal;
    letter-spacing: 1.2px;
    line-height: 1.3;
    margin-top: 36px;
  }
  .reach { margin-top: 22px; list-style: none; }
  .reach li {
    display: flex;
    justify-content: flex-end;
    align-items: center;
    gap: 10px;
    color: var(--text-grey);
    font-size: 15px;
    letter-spacing: 1.1px;
    line-height: 1.4;
  }
  .reach .web-name { color: var(--brand-blue); }
  .reach svg { width: 14px; height: 14px; fill: var(--brand-blue); flex: none; }
</style>
</head>
<body>
  <section class="card card-back" aria-label="Card back">
    <div class="back-lockup">
      <div class="back-square"></div>
      <div class="back-words">
        <div class="back-name">Dorsey K. Wendell</div>
        <div class="back-trade">Heating &amp; Plumbing</div>
      </div>
    </div>
  </section>

  <section class="card card-front" aria-label="Card front">
    <div class="front-mark">
      <div class="front-square"></div>
      <div class="front-company">Dorsey K. Wendell</div>
    </div>
    <div class="contact">
      <div class="person-name">Russell T. Wendell</div>
      <div class="person-title">President</div>
      <div class="license">PA #093148</div>
      <address class="address">5187 W. Cedar Brook Rd.<br>Larkston, PA 17632</address>
      <ul class="reach">
        <li>(717) 592-0817
          <svg viewBox="0 0 14 14"><path d="M4 0h6a1.5 1.5 0 0 1 1.5 1.5v11A1.5 1.5 0 0 1 10 14H4a1.5 1.5 0 0 1-1.5-1.5v-11A1.5 1.5 0 0 1 4 0zm0 2v9h6V2zm3 9.6a.8.8 0 1 0 0 1.6.8.8 0 0 0 0-1.6z"/></svg>
        </li>
        <li>russelltwendell@fernmail.net
          <svg viewBox="0 0 14 14"><path d="M0 3h14v1L7 8 0 4zm0 2.3 7 4 7-4V11H0z"/></svg>
        </li>
        <li><span>www.<span class="web-name">dorseykwendell</span>.net</span>
          <svg viewBox="0 0 14 14"><path d="M7 0a7 7 0 1 0 0 14A7 7 0 0 0 7 0zm0 1.5a5.5 5.5 0 1 1 0 11 5.5 5.5 0 0 1 0-11zM3 5h3v3H4zm5 1h3v4H9z"/></svg>
        </li>
      </ul>
    </div>
  </section>
</body>
</html>
```